Self Storage facility in South Africa needs marketing flyers

We are a self storage facility in Stellenbosch, South Africa. We are looking for 3 flyers to target our 3 primary markets. 1) Students - in college (university) accomodation or apartments close by with limited storage space2) Households - more general population. People moving house or renovating and just need extra space to declutter their lives.3) Business - Document storage is an area that we believe is in demand. We would like the key elements of the flyer to highlight the benefits of BoxHaven. The imagery and copy for each variation should be crafted for that specific audience.Attached are some images of the facility and our Logo. I've attached a print ad to give an example of recent work. This is by no means what I would like the flyer to look like - just an example of previous work.Happy for royalty free stock photography to be used Our website (old, in redesign) is www.boxhavenza.co.za

Requirements
Must have
• Emotive pictures highlighting either use of storage or freedom gained from use of storage (eg people having time and space to do what they want)

```html
<!DOCTYPE html>
<html lang="en">
<head>
<meta charset="utf-8">
<title>BoxHaven – Business Storage Solutions</title>
<link rel="stylesheet" href="https://fonts.googleapis.com/css2?family=Poppins:wght@700;800;900&family=Raleway:wght@300;400&display=swap">
<style>
  :root {
    --orange: #f9a75a;
    --icon-orange: #f7a556;
    --slate: #344b59;
    --text-slate: #3e5463;
    --white: #ffffff;
    --ink: #111111;
  }
  * { margin: 0; padding: 0; box-sizing: border-box; }
  html, body { width: 1200px; height: 818px; overflow: hidden; }
  body { background: var(--orange); position: relative; font-family: 'Raleway', sans-serif; }

  .photo-panel {
    position: absolute; left: 24px; top: 24px; width: 727px; height: 770px;
    background:
      radial-gradient(ellipse 30% 55% at 78% 55%, rgba(150,155,160,.55), transparent 70%),
      linear-gradient(90deg, #2c2f33 0%, #3b3e42 35%, #55595d 60%, #6b6f73 80%, #5a5e62 100%);
    overflow: hidden;
  }
  .accent-bar { position: absolute; width: 50px; height: 9px; background: var(--orange); top: 66px; }
  .headline {
    position: absolute; top: 82px; color: var(--white);
    font-family: 'Poppins', sans-serif; font-weight: 800; font-size: 26px; line-height: 42px;
    letter-spacing: -0.3px;
  }
  .question { left: 82px; }
  .answer { left: 517px; top: 78px; }
  .contact {
    position: absolute; left: 517px; top: 212px; color: var(--white);
    font-size: 18.5px; line-height: 23.2px; font-weight: 400;
  }
  .service-banner {
    position: absolute; left: 160px; top: 720px; width: 472px; height: 56px;
    background: var(--slate); color: var(--white);
    font-weight: 300; font-size: 32px; line-height: 56px; text-align: center;
  }

  .benefits-panel {
    position: absolute; left: 775px; top: 24px; width: 401px; height: 770px; background: var(--white);
  }
  .benefit { position: absolute; left: 30px; display: flex; align-items: center; }
  .benefit svg { width: 82px; height: 76px; flex: none; }
  .benefit-label { margin-left: 16px; color: var(--text-slate); font-size: 25px; line-height: 35px; }

  .cover-line {
    position: absolute; left: 0; width: 100%; text-align: center;
    color: var(--slate); font-family: 'Poppins', sans-serif; font-weight: 900; letter-spacing: -1px;
  }
  .cover-small { top: 538px; font-size: 36px; line-height: 44px; }
  .cover-large { top: 576px; font-size: 58px; line-height: 70px; }

  .brand {
    position: absolute; left: 0; top: 690px; width: 100%;
    display: flex; justify-content: center; align-items: center; gap: 12px;
  }
  .brand-mark { width: 30px; height: 30px; background: var(--ink); }
  .brand-name { font-family: 'Poppins', sans-serif; font-weight: 700; font-size: 46px; color: var(--ink); letter-spacing: -1px; }
</style>
</head>
<body>
  <section class="photo-panel" role="img" aria-label="Photo of an archive aisle with shelves full of labelled document boxes">
    <div class="accent-bar" style="left:82px"></div>
    <h1 class="headline question">Are you looking for an<br>organized document<br>storage facility?</h1>
    <div class="accent-bar" style="left:517px"></div>
    <h2 class="headline answer">We have<br>the perfect<br>solution.</h2>
    <address class="contact" style="font-style:normal">
      14 Willow Lane<br>Oakridge<br>Stellenbosch 7611<br>+27 21 555 0142<br>info@boxhavenza.co.za<br>www.boxhavenza.co.za
    </address>
    <div class="service-banner">Business Storage Solutions</div>
  </section>

  <aside class="benefits-panel">
    <div class="benefit" style="top:28px">
      <svg viewBox="0 0 82 76" fill="var(--icon-orange)"><path d="M14 8 L82 30 L72 46 L8 26 Z"/><rect x="3" y="36" width="4" height="24"/><rect x="3" y="42" width="34" height="6"/><rect x="36" y="34" width="5" height="22"/><circle cx="40" cy="30" r="3" fill="#fff"/></svg>
      <span class="benefit-label">Focused on Security</span>
    </div>
    <div class="benefit" style="top:122px">
      <svg viewBox="0 0 82 76" fill="var(--icon-orange)"><rect x="4" y="4" width="6" height="40" transform="rotate(-45 7 24)"/><path d="M34 34 L52 48 L38 62 L26 48 Z"/><path d="M52 48 L72 58 L48 82 L38 62 Z"/><rect x="16" y="58" width="12" height="5"/><rect x="6" y="68" width="30" height="5"/></svg>
      <span class="benefit-label">Neat Storage Facilities</span>
    </div>
    <div class="benefit" style="top:214px">
      <svg viewBox="0 0 82 76" fill="none" stroke="var(--icon-orange)" stroke-width="5"><path d="M3 16 Q14 4 24 18 L54 52 L80 28"/><rect x="38" y="4" width="28" height="28" fill="var(--icon-orange)" transform="rotate(45 52 18)"/><circle cx="54" cy="64" r="7" fill="var(--icon-orange)"/></svg>
      <span class="benefit-label">Convenient Moving</span>
    </div>
    <div class="benefit" style="top:318px">
      <svg viewBox="0 0 82 76" fill="none" stroke="var(--icon-orange)" stroke-width="4"><rect x="26" y="4" width="50" height="48"/><path d="M12 4 V52 M5 12 L12 4 L19 12 M5 44 L12 52 L19 44"/><path d="M26 66 H76 M32 60 L26 66 L32 72 M70 60 L76 66 L70 72"/></svg>
      <span class="benefit-label">Variety of Sizes</span>
    </div>
    <div class="benefit" style="top:420px">
      <svg viewBox="0 0 82 76" fill="var(--icon-orange)"><path d="M2 30 L41 2 L80 30 L76 34 L41 9 L6 34 Z"/><path d="M10 32 L41 12 L72 32 V76 H64 V40 H18 V76 H10 Z"/><rect x="20" y="44" width="42" height="3"/><rect x="20" y="50" width="42" height="3"/><path d="M26 70 V62 L30 56 H52 L56 62 V70 Z"/><rect x="36" y="22" width="10" height="10"/></svg>
      <span class="benefit-label">Variety of Storage<br>Options</span>
    </div>

    <div class="cover-line cover-small">WE HAVE YOU</div>
    <div class="cover-line cover-large">COVERED</div>

    <div class="brand">
      <span class="brand-mark"></span>
      <span class="brand-name">BoxHaven</span>
    </div>
  </aside>
</body>
</html>
```